Vorbanix Stationery Design Project

We need a stationery design for our new business Vorbanix which deals in advanced cleaning technologies such as Ultrasonic cleaning and high pressure cleaning machinery.

Our colour scheme is as per the included files.

We require business cards, letterheads, a brochure folder and email signatures design
Updates

Project Deadline Extended

Apologies for the delay in making a decision on this project. We will be making a final decision during the course of next week

Target Market(s)

Industries ranging from medical, automotive, mining, engineering all requiring specialised cleaning services

Industry/Entity Type

Pressure Cleaning

Requirements
Must have
• Please include our supplied logo and colour scheme. The design needs to be professional but creative.

```html
<!DOCTYPE html>
<html lang="en">
<head>
<meta charset="utf-8">
<title>Vorbanix Business Card</title>
<link rel="stylesheet" href="https://fonts.googleapis.com/css2?family=Archivo+Black&family=Open+Sans:wght@400;600;700&display=swap">
<style>
  :root {
    --backdrop: #e4e6ec;
    --navy: #1d3378;
    --royal: #24489e;
    --deep: #172a62;
    --silver: #c9ccd2;
    --grey-brand: #8c8e93;
    --grey-soft: #a4a6ab;
    --cyan: #2fa9e4;
    --white: #ffffff;
  }
  * { box-sizing: border-box; margin: 0; padding: 0; }
  html, body { width: 1200px; height: 797px; overflow: hidden; }
  body {
    background: var(--backdrop);
    font-family: "Open Sans", Arial, sans-serif;
    position: relative;
  }
  .card {
    position: absolute;
    top: 244px;
    width: 540px;
    height: 309px;
    overflow: hidden;
    box-shadow: 0 6px 18px rgba(30, 40, 70, 0.18);
  }
  /* Back side */
  .card-back { left: 40px; background: var(--navy); }
  .back-texture {
    position: absolute;
    inset: 0;
    background: linear-gradient(160deg, var(--royal) 0%, var(--navy) 55%, var(--deep) 100%);
  }
  .tagline {
    position: absolute;
    top: 78px;
    left: 0;
    width: 100%;
    text-align: center;
    font-family: "Archivo Black", Arial, sans-serif;
    font-weight: 400;
    color: var(--silver);
    line-height: 1;
  }
  .tagline .line-lg { display: block; font-size: 33px; letter-spacing: 0.3px; }
  .tagline .line-mid { display: block; font-size: 33px; margin-top: 2px; }
  .tagline .line-mid small { font-size: 17px; }
  .tagline .line-sm { display: block; font-size: 19px; margin-top: 2px; padding-left: 150px; }
  .web {
    position: absolute;
    bottom: 34px;
    width: 100%;
    text-align: center;
    font-size: 15px;
    font-weight: 700;
    color: var(--cyan);
    letter-spacing: 0.3px;
  }
  /* Front side */
  .card-front { left: 620px; background: var(--white); }
  .card-front .band { position: absolute; inset: 0; }
  .brand {
    position: absolute;
    top: 40px;
    left: 110px;
    display: flex;
    align-items: center;
    gap: 14px;
  }
  .brand-mark {
    width: 46px;
    height: 46px;
    background: var(--royal);
  }
  .brand-name {
    font-size: 40px;
    font-weight: 700;
    color: var(--grey-brand);
    letter-spacing: 1px;
    line-height: 1;
  }
  .brand-sub {
    position: absolute;
    top: 90px;
    left: 170px;
    font-size: 15px;
    color: var(--grey-soft);
  }
  .holder {
    position: absolute;
    left: 28px;
    bottom: 50px;
    color: var(--white);
  }
  .holder-name { font-size: 17px; letter-spacing: 0.3px; }
  .holder-role { font-size: 13px; color: var(--cyan); margin-top: 2px; }
  .contact {
    position: absolute;
    left: 300px;
    top: 176px;
    color: var(--white);
    font-size: 11.5px;
    line-height: 1.35;
  }
  .contact-row { display: flex; align-items: flex-start; gap: 6px; margin-bottom: 3px; }
  .contact-row svg { flex: none; margin-top: 2px; }
  .contact-pair { display: flex; gap: 16px; }
</style>
</head>
<body>
  <section class="card card-back" aria-label="Business card back">
    <div class="back-texture" role="img" aria-label="Faceted blue geometric background pattern"></div>
    <h2 class="tagline">
      <span class="line-lg">Ultrasonic cleaning</span>
      <span class="line-mid"><small>and</small> High pressure</span>
      <span class="line-sm">cleaning machinery</span>
    </h2>
    <p class="web">www.VORBANIX.com</p>
  </section>

  <section class="card card-front" aria-label="Business card front">
    <svg class="band" viewBox="0 0 540 309" aria-hidden="true">
      <defs>
        <linearGradient id="bandFill" x1="0" y1="0" x2="0" y2="1">
          <stop offset="0" stop-color="#24489e"/>
          <stop offset="1" stop-color="#1a2e6e"/>
        </linearGradient>
        <linearGradient id="swoosh" x1="0" y1="0" x2="1" y2="0">
          <stop offset="0" stop-color="#c8cacf" stop-opacity="0"/>
          <stop offset="0.5" stop-color="#9a9ca2"/>
          <stop offset="1" stop-color="#c8cacf" stop-opacity="0.3"/>
        </linearGradient>
      </defs>
      <path d="M0 212 Q 290 150 540 122 L540 309 L0 309 Z" fill="url(#bandFill)"/>
      <path d="M50 196 Q 290 128 520 112 Q 290 138 50 200 Z" fill="url(#swoosh)"/>
    </svg>

    <div class="brand">
      <span class="brand-mark"></span>
      <span class="brand-name">VORBANIX</span>
    </div>
    <p class="brand-sub">Advanced Cleaning Technologies</p>

    <div class="holder">
      <p class="holder-name">CARDHOLDER NAME</p>
      <p class="holder-role">Designation</p>
    </div>

    <div class="contact">
      <div class="contact-row">
        <svg width="10" height="12" viewBox="0 0 10 12" aria-hidden="true"><path d="M5 0a4 4 0 0 0-4 4c0 3 4 8 4 8s4-5 4-8a4 4 0 0 0-4-4z" fill="#2fa9e4"/><circle cx="5" cy="4" r="1.5" fill="#1d3378"/></svg>
        <span>01 01 Avenue, Suite No. 123,<br>Your City, Country</span>
      </div>
      <div class="contact-pair">
        <div class="contact-row">
          <svg width="11" height="11" viewBox="0 0 12 12" aria-hidden="true"><circle cx="6" cy="6" r="6" fill="#2fa9e4"/><path d="M4 3l1.2 1.4-.7.8a4 4 0 0 0 2.3 2.3l.8-.7L9 8 8 9c-2.5-.3-4.7-2.5-5-5z" fill="#1d3378"/></svg>
          <span>012 345 6789</span>
        </div>
        <div class="contact-row">
          <svg width="12" height="11" viewBox="0 0 12 11" aria-hidden="true"><rect x="0" y="4" width="12" height="7" rx="1" fill="#2fa9e4"/><rect x="3" y="0" width="6" height="5" fill="#2fa9e4"/></svg>
          <span>012 345 6780</span>
        </div>
      </div>
      <div class="contact-row">
        <svg width="12" height="9" viewBox="0 0 12 9" aria-hidden="true"><rect width="12" height="9" rx="1" fill="#2fa9e4"/><path d="M1 1l5 4 5-4" stroke="#1d3378" fill="none"/></svg>
        <span>name@vorbanix.com</span>
      </div>
    </div>
  </section>
</body>
</html>
```